Can you create a Business Card based on the Logo you designed.

See example and would like to see other examples.

Trying to keep it very clean with a focus on the logo and name.

```html
<!DOCTYPE html>
<html lang="en">
<head>
<meta charset="utf-8">
<title>Verdano Business Card</title>
<link rel="stylesheet" href="https://fonts.googleapis.com/css2?family=Nunito:wght@700;800&family=Arimo:wght@400;700&display=swap">
<style>
  :root {
    --backdrop: #bebdbe;
    --card-white: #ffffff;
    --green-deep: #1f8a4c;
    --green-dark: #27894f;
    --green-leaf: #8cc63f;
    --green-name: #6abd45;
    --orange: #f4a94b;
    --text-grey: #6b6b6b;
    --rule-grey: #dcdcdc;
  }
  * { box-sizing: border-box; margin: 0; padding: 0; }
  html, body { width: 1200px; height: 876px; overflow: hidden; }
  body {
    background: var(--backdrop);
    position: relative;
    font-family: "Arimo", Arial, sans-serif;
  }
  .card {
    position: absolute;
    width: 525px;
    height: 300px;
    border-radius: 20px;
    overflow: hidden;
    box-shadow: 0 10px 24px rgba(0,0,0,0.22);
  }
  /* Front */
  .card-front {
    left: 120px; top: 110px;
    background: var(--card-white);
  }
  .front-brand {
    position: absolute;
    left: 40px; top: 0; width: 220px; height: 270px;
    display: flex; align-items: center; justify-content: center; gap: 8px;
  }
  .brand-name {
    font-family: "Nunito", sans-serif;
    font-weight: 800;
    font-size: 46px;
    letter-spacing: 0.5px;
    color: var(--green-dark);
  }
  .brand-dot {
    width: 16px; height: 16px; border-radius: 50%;
    background: var(--orange);
    align-self: flex-start;
    margin-top: 104px;
  }
  .front-divider {
    position: absolute;
    left: 268px; top: 70px; width: 1px; height: 130px;
    background: var(--rule-grey);
  }
  .front-details {
    position: absolute;
    left: 290px; top: 82px;
  }
  .person-name {
    font-weight: 700; font-size: 22px; color: var(--green-name);
  }
  .person-role {
    font-size: 15px; color: var(--text-grey); margin-top: 4px; margin-bottom: 14px;
  }
  .contact-line {
    display: flex; align-items: center; gap: 8px;
    font-size: 15px; color: var(--text-grey); line-height: 23px;
  }
  .contact-line svg { width: 12px; height: 12px; flex: none; }
  .front-stripe {
    position: absolute; left: 0; bottom: 0; width: 100%; height: 26px;
    display: flex;
  }
  .stripe-deep { background: var(--green-deep); width: 28%; }
  .stripe-leaf { background: var(--green-leaf); width: 38%; }
  .stripe-orange { background: var(--orange); flex: 1; }
  /* Back */
  .card-back {
    left: 555px; top: 460px;
  }
  .back-pattern {
    position: absolute; inset: 0;
    background: radial-gradient(circle at 40% 35%, #2a9a5c 0%, var(--green-deep) 55%, #187a42 100%);
  }
  .back-brand {
    position: absolute; inset: 0;
    display: flex; align-items: center; justify-content: center; gap: 10px;
  }
  .back-brand .brand-name { color: var(--card-white); font-size: 54px; }
  .back-brand .brand-dot { margin-top: 0; align-self: center; width: 18px; height: 18px; }
</style>
</head>
<body>
  <section class="card card-front">
    <div class="front-brand">
      <span class="brand-name">Verdano</span>
    </div>
    <div class="front-divider"></div>
    <div class="front-details">
      <p class="person-name">Elias Marrow</p>
      <p class="person-role">Chief Executive Officer</p>
      <p class="contact-line">
        <svg viewBox="0 0 12 12"><path d="M3 1l2 2.5-1.2 1.2c.7 1.4 1.8 2.5 3.2 3.2L8.2 6.7 11 8.6 9.8 11C5 10.6 1.4 7 1 2.2z" fill="var(--green-name)"/></svg>
        +1 (555) 014-2208
      </p>
      <p class="contact-line">
        <svg viewBox="0 0 12 12"><rect x="1" y="2.5" width="10" height="7" rx="1" fill="none" stroke="var(--green-name)" stroke-width="1.3"/><path d="M1.5 3l4.5 3.5L10.5 3" fill="none" stroke="var(--green-name)" stroke-width="1.3"/></svg>
        ceo@verdano.com
      </p>
      <p class="contact-line">
        <svg viewBox="0 0 12 12"><circle cx="6" cy="6" r="5" fill="var(--green-name)"/><path d="M1 6h10M6 1c-2.5 2.8-2.5 7.2 0 10M6 1c2.5 2.8 2.5 7.2 0 10" fill="none" stroke="#fff" stroke-width="0.8"/></svg>
        www.verdano.com
      </p>
    </div>
    <div class="front-stripe">
      <div class="stripe-deep"></div>
      <div class="stripe-leaf"></div>
      <div class="stripe-orange"></div>
    </div>
  </section>

  <section class="card card-back">
    <div class="back-pattern" role="img" aria-label="Faint repeating leaf pattern on deep green"></div>
    <div class="back-brand">
      <span class="brand-name">Verdano</span>
      <span class="brand-dot"></span>
    </div>
  </section>
</body>
</html>
```